Business card design for industrial spray painting - startup business

Design the layout of our new business card using the logo we have provided.

We want the card to be matt black in colour.

We only want our logo and slogan on the face side.

Because the card is black we would like the slogan WE PAINT ANYTHING! to be in white.

We want our information on the rear side.

I would like my name in blue matching the blue in the logo.

The remainder of the information should be in grey to match the grey in the logo.

The overall finish should look minimal, clean and slick.

Our business is industrlal and of a masculine nature.

Target Market(s)

industrial and mining companies

Contact Information for Business Card

(front of card – matt black)
insert logo here:
insert this tag line: WE PAINT ANYTHING!

--------------------------------------------------------------------------------------------------------------

(back of card – matt black)
Dorian Kestle
Paint and Coatings Specialist
47 Millbrook Avenue, Bayswater WA 6053
M: +61 437 281 914
T: +61 8 555 7318
E: dorian@coatlynx.co
W: www.coatlynx.co

Font styles to use
Sans Serif

Colors
000000
0455a3

Requirements
Must have
• clean, slick minimalist look. Masculine as we deal mostly with industrial spray painting

```html
<!DOCTYPE html>
<html lang="en">
<head>
<meta charset="utf-8">
<title>Coatlynx Business Card</title>
<link href="https://fonts.googleapis.com/css2?family=Roboto:wght@300;400&display=swap" rel="stylesheet">
<style>
  :root {
    --stage: #2a2d32;
    --card: #0b0b0c;
    --brand-blue: #1a7fd4;
    --brand-grey: #8f9296;
    --slogan: #d9dadb;
  }
  * { margin: 0; padding: 0; box-sizing: border-box; }
  html, body {
    width: 1200px;
    height: 900px;
    overflow: hidden;
    background: var(--stage);
    font-family: "Roboto", Arial, sans-serif;
  }
  .stage {
    width: 1200px;
    height: 900px;
    display: flex;
    align-items: center;
    justify-content: center;
    gap: 40px;
  }
  .card {
    width: 540px;
    height: 309px;
    background: var(--card);
    border-radius: 22px;
    position: relative;
    box-shadow: 0 12px 30px rgba(0,0,0,0.45);
  }
  /* Rear side: contact details */
  .card--details .holder-name {
    position: absolute;
    left: 34px;
    top: 30px;
    color: var(--brand-blue);
    font-size: 32px;
    font-weight: 400;
    letter-spacing: -0.3px;
  }
  .card--details .details {
    position: absolute;
    left: 250px;
    top: 104px;
    color: var(--brand-grey);
    font-size: 16px;
    font-weight: 400;
    line-height: 20px;
    list-style: none;
  }
  .card--details .details .role { margin-bottom: 16px; }
  .card--details .details .gap { margin-top: 10px; }

  /* Face side: brand and slogan */
  .card--face {
    display: flex;
    flex-direction: column;
    align-items: center;
    justify-content: center;
  }
  .brand {
    display: flex;
    align-items: center;
    gap: 14px;
  }
  .brand-mark {
    width: 34px;
    height: 34px;
    background: var(--brand-blue);
  }
  .brand-name {
    color: var(--brand-blue);
    font-size: 40px;
    font-weight: 300;
    letter-spacing: 3px;
    text-transform: uppercase;
  }
  .slogan {
    margin-top: 26px;
    color: var(--slogan);
    font-size: 16px;
    font-weight: 300;
    letter-spacing: 0.5px;
  }
</style>
</head>
<body>
  <main class="stage">
    <section class="card card--details" aria-label="Business card rear side">
      <h1 class="holder-name">Dorian Kestle</h1>
      <ul class="details">
        <li class="role">Paint &amp; Coatings Specialist</li>
        <li>+61 437 281 914</li>
        <li>+61 8 555 7318</li>
        <li class="gap">47 Millbrook Avenue</li>
        <li>Harrowdale WA 6053</li>
        <li class="gap">dorian@coatlynx.co</li>
        <li>www.coatlynx.co</li>
      </ul>
    </section>

    <section class="card card--face" aria-label="Business card face side">
      <div class="brand">
        <span class="brand-mark" aria-hidden="true"></span>
        <span class="brand-name">Coatlynx</span>
      </div>
      <p class="slogan">We paint anything!</p>
    </section>
  </main>
</body>
</html>
```